lunavo GmbH needs great looking businesscards to leave an impression

Dear Designers,

Our company lunavo GmbH based in switzerland needs to have impressive businesscards. We produce and sell high quality bleaching products for the upper market.
We'd like to have a minimalistic but still meaningful design. You'll fine our company logo attached and some of our packaging designs. Our company slogan is "discover your smile". If you need additional information feel free to contact us.
Kind Regards Milo

Dear Designers, This is a business card design contest! I try to call the support to fix that. Kind Regards Milo

```html
<!DOCTYPE html>
<html lang="de">
<head>
<meta charset="utf-8">
<title>lunavo GmbH – Visitenkarte</title>
<link rel="stylesheet" href="https://fonts.googleapis.com/css2?family=PT+Sans:wght@400;700&display=swap">
<style>
  :root {
    --stage: #4b4b4b;
    --card: #ffffff;
    --card-texture: #f3f3f4;
    --teal: #22575f;
    --mauve: #a27170;
    --rose: #d9867e;
    --ink: #1c1c1c;
    --name-ink: #ffffff;
  }
  * { box-sizing: border-box; margin: 0; padding: 0; }
  html, body { width: 1200px; height: 900px; overflow: hidden; }
  body {
    background: var(--stage);
    font-family: "PT Sans", sans-serif;
    position: relative;
  }
  .card {
    position: absolute;
    left: 320px;
    width: 560px;
    height: 320px;
    background: var(--card);
    overflow: hidden;
    box-shadow: 0 10px 28px rgba(0,0,0,.35);
  }
  .card--back { top: 100px; }
  .card--front { top: 480px; }

  /* back side */
  .card__texture {
    position: absolute; inset: 0;
    background: var(--card-texture);
  }
  .name-tab {
    position: absolute;
    top: 40px; right: 0;
    width: 250px; height: 50px;
    background: var(--teal);
    border-radius: 25px 0 0 25px;
    border: 3px solid #ffffff;
    border-right: none;
    box-shadow: 0 3px 6px rgba(0,0,0,.25);
    display: flex; align-items: center; justify-content: center;
    color: var(--name-ink);
    font-size: 25px;
    letter-spacing: .5px;
  }
  .contact {
    position: absolute;
    right: 28px; top: 130px;
    text-align: right;
    list-style: none;
    color: var(--ink);
    font-size: 17px;
    line-height: 1.45;
  }

  /* front side */
  .accent-band {
    position: absolute;
    top: 0; right: 0;
    width: 150px; height: 100%;
    background: linear-gradient(90deg, var(--rose) 0%, var(--mauve) 30%, var(--teal) 60%, var(--teal) 100%);
  }
  .brand {
    position: absolute;
    left: 54px; top: 128px;
    display: flex; align-items: center; gap: 14px;
  }
  .brand__dot {
    width: 46px; height: 46px; border-radius: 50%;
    background: var(--rose);
  }
  .brand__name {
    font-size: 54px;
    font-weight: 400;
    color: var(--teal);
    line-height: 1;
    letter-spacing: 1px;
  }
</style>
</head>
<body>
  <section class="card card--back" aria-label="Rückseite der Visitenkarte">
    <div class="card__texture" role="img" aria-label="Feines Punktmuster als Hintergrund"></div>
    <div class="name-tab">Lena Marwick</div>
    <ul class="contact">
      <li>Address: Lindenweg 14, 8045, Zürich</li>
      <li>Mobil: 0041 79 555 40 80</li>
      <li>Mail: lena.marwick@mailbox.ch</li>
    </ul>
  </section>

  <section class="card card--front" aria-label="Vorderseite der Visitenkarte">
    <div class="accent-band" role="img" aria-label="Dekoratives Farbband in Rosé, Mauve und Petrol"></div>
    <div class="brand">
      <span class="brand__dot"></span>
      <span class="brand__name">lunavo</span>
    </div>
  </section>
</body>
</html>
```